Business Card Design for new social media business

I am looking for a new professional business card design for an exciting new company which is based on providing members with experiences of others to benefit their choice of places to visit for restaurants, bars, clubs, national monument, tourist sights, hotels and so forth.
Updates

Please submit designs as I will choose to commit the funds depending on designs.

Reason: More designs required

Target Market(s)

Business Managers as well as directors alongside owners

Industry/Entity Type

Business

Requirements
Must have
• Logo design and symbols
Nice to have
• Logo / Symbol on the back of the business card and possibly the logo as if embedded/embossed on the business card.

```html
<!DOCTYPE html>
<html lang="en">
<head>
<meta charset="utf-8">
<title>Roamwell business card</title>
<link rel="stylesheet" href="https://fonts.googleapis.com/css2?family=Arvo:wght@700&family=Quicksand:wght@500;700&display=swap">
<style>
  :root {
    --backdrop: #dcdcdc;
    --card: #ecebe7;
    --band-red: #d9471f;
    --band-amber: #e39412;
    --band-black: #1f1f1f;
    --hatch: #c8c8c6;
    --ink: #1c1c1c;
    --band-text: #f6eee2;
  }
  html, body {
    margin: 0;
    width: 1200px;
    height: 1152px;
    overflow: hidden;
    background: var(--backdrop);
  }
  .card {
    position: absolute;
    width: 900px;
    height: 531px;
    box-shadow: 0 12px 30px rgba(0,0,0,0.28);
  }
  .card--front { left: 60px; top: 30px; }
  .card--back { left: 240px; top: 591px; }
  .card-surface { fill: var(--card); }
  .band-red { fill: var(--band-red); }
  .band-amber { fill: var(--band-amber); }
  .band-black { fill: var(--band-black); }
  .hatch-field { fill: var(--hatch); }
  .holder-name {
    font-family: "Arvo", Georgia, serif;
    font-weight: 700;
    font-size: 64px;
    fill: var(--ink);
  }
  .band-line {
    font-family: "Quicksand", Arial, sans-serif;
    font-weight: 500;
    font-size: 24px;
    fill: var(--band-text);
  }
  .brand-name {
    font-family: "Quicksand", Arial, sans-serif;
    font-weight: 700;
    font-size: 68px;
    fill: var(--ink);
  }
  .brand-dot { fill: var(--band-red); }
</style>
</head>
<body>

<svg class="card card--front" viewBox="0 0 1000 590" xmlns="http://www.w3.org/2000/svg">
  <rect class="card-surface" width="1000" height="590"/>
  <g role="img" aria-label="Diagonal hatched stripe pattern">
    <polygon class="hatch-field" points="0,290 1000,590 0,590"/>
  </g>
  <polygon class="band-red" points="0,95 1000,395 1000,450 0,150"/>
  <polygon class="band-amber" points="0,160 1000,460 1000,515 0,215"/>
  <polygon class="band-black" points="0,225 1000,525 1000,580 0,280"/>

  <text class="holder-name" x="960" y="368" text-anchor="end" transform="rotate(16.7 960 368)">Rohan Mehta</text>
  <text class="band-line" x="910" y="403" text-anchor="end" transform="rotate(16.7 910 403)">Work Manager</text>
  <text class="band-line" x="900" y="465" text-anchor="end" transform="rotate(16.7 900 465)">roamwell@email.com</text>
  <text class="band-line" x="880" y="524" text-anchor="end" transform="rotate(16.7 880 524)">social.example/rohan.mehta</text>
</svg>

<svg class="card card--back" viewBox="0 0 1000 590" xmlns="http://www.w3.org/2000/svg">
  <rect class="card-surface" width="1000" height="590"/>
  <g role="img" aria-label="Diagonal hatched stripe pattern">
    <polygon class="hatch-field" points="0,0 1000,0 1000,112 0,412"/>
  </g>
  <polygon class="band-red" points="0,420 1000,120 1000,175 0,475"/>
  <polygon class="band-amber" points="0,485 1000,185 1000,240 0,540"/>
  <polygon class="band-black" points="0,550 1000,250 1000,305 0,605"/>

  <text class="band-line" x="100" y="425" transform="rotate(-16.7 100 425)">218 Harbour Lane, Westbrook NY 10234</text>
  <text class="band-line" x="140" y="478" transform="rotate(-16.7 140 478)">tel: 5550 1234  /  fax: 5550 1235</text>
  <text class="band-line" x="160" y="537" transform="rotate(-16.7 160 537)">www.roamwell.com</text>

  <g class="brand" transform="rotate(-16.7 620 520)">
    <circle class="brand-dot" cx="590" cy="497" r="22"/>
    <text class="brand-name" x="630" y="520">roamwell</text>
  </g>
</svg>

</body>
</html>
```